Business Card Design Project

I need a business card with the logo i have selected with a heading of
Repairs
Restretching
Cleaning
Supply and lay all in that order
call 0438271946
www.rugmendhouse.example

colours used should be bold and clear and match the logo, thinking white background with black writing
a mixture of fonts is okay but Repairs, Cleaning, Supply and Lay should all be the same as they are the main points...
kind regards lorn
update to all designers i would like my name on the business card Lorn Tabbet i think it would look good above the phone number
Updates

can you please add my name on the business card

Lorn Tabbet

i think it would look best above the phone numberĀ 

Industry/Entity Type

Business

```html
<!DOCTYPE html>
<html lang="en">
<head>
<meta charset="utf-8">
<title>Rugmend House – Business Card</title>
<link rel="stylesheet" href="https://fonts.googleapis.com/css2?family=Signika:wght@600;700&family=Coustard:wght@900&display=swap">
<style>
  :root {
    --backdrop: #d6d6d6;
    --card-white: #ffffff;
    --brand-red: #e01e26;
    --brand-red-deep: #c8171f;
    --brand-navy: #123f66;
    --ink-black: #111111;
    --accent-orange: #f6a21e;
  }
  * { margin: 0; padding: 0; box-sizing: border-box; }
  html, body {
    width: 1200px;
    height: 900px;
    overflow: hidden;
    background: var(--backdrop);
  }
  .business-card {
    position: absolute;
    left: 80px;
    top: 150px;
    width: 1040px;
    height: 600px;
    border-radius: 40px;
    overflow: hidden;
    background: var(--card-white);
    box-shadow: 0 18px 40px rgba(0,0,0,0.18);
  }
  .card-swoosh {
    position: absolute;
    inset: 0;
    width: 100%;
    height: 100%;
  }
  .brand-block {
    position: absolute;
    left: 50px;
    top: 150px;
    width: 420px;
    display: flex;
    flex-direction: column;
    align-items: center;
    gap: 28px;
  }
  .brand-dot {
    width: 110px;
    height: 110px;
    border-radius: 50%;
    background: var(--brand-red);
  }
  .brand-name {
    font-family: "Signika", sans-serif;
    font-weight: 700;
    font-size: 74px;
    line-height: 0.95;
    color: var(--brand-navy);
    text-align: center;
    text-transform: uppercase;
  }
  .service-list {
    position: absolute;
    left: 620px;
    top: 40px;
    width: 380px;
    list-style: none;
    text-align: center;
    font-family: "Signika", sans-serif;
    font-weight: 600;
    font-size: 44px;
    color: var(--card-white);
  }
  .service-list li { height: 76px; line-height: 76px; }
  .contact-block {
    position: absolute;
    left: 560px;
    top: 370px;
    width: 450px;
    font-family: "Coustard", serif;
    font-weight: 900;
  }
  .contact-name {
    font-size: 40px;
    color: var(--ink-black);
    margin-left: 70px;
  }
  .contact-phone {
    font-size: 40px;
    color: var(--accent-orange);
    margin-top: 14px;
    margin-left: 40px;
  }
  .contact-web {
    font-size: 25px;
    color: var(--accent-orange);
    margin-top: 12px;
    margin-left: 8px;
  }
</style>
</head>
<body>
  <main class="business-card">
    <svg class="card-swoosh" viewBox="0 0 1040 600" preserveAspectRatio="none" aria-hidden="true">
      <path d="M520 0 Q650 220 430 600 L1040 600 L1040 0 Z" fill="var(--brand-navy)"/>
      <path d="M600 0 Q690 260 420 600 L1040 600 L1040 0 Z" fill="var(--brand-red)"/>
    </svg>

    <div class="brand-block">
      <div class="brand-dot"></div>
      <div class="brand-name">Rugmend<br>House</div>
    </div>

    <ul class="service-list">
      <li>Repairs</li>
      <li>Restretching</li>
      <li>Cleaning</li>
      <li>Supply and Lay</li>
    </ul>

    <div class="contact-block">
      <p class="contact-name">Lorn Tabbet</p>
      <p class="contact-phone">call 0438271946</p>
      <p class="contact-web">www.rugmendhouse.example</p>
    </div>
  </main>
</body>
</html>
```